Business card on Pvc transparent frosted

I need a business advertising card that will be eye catching and fun.
Target Market(s)
Rednecks, country, hunters, Fisherman, ATV users, lifted trucks, cowboys, cattle ranchers, farmers, etc
Industry/Entity Type
Apparel Store
Contact Information for Business Card
This will he printed on single side of a transparent frosted plastic card with shinny foil print option.
Requirements
Must have
- 1 - My logo.
- 2 - HOLLER HOLLOW OUTFITTERS
- 3 - my motto "Built for the back roads..... Dressed for the DIRT we love!!"; 4 - my website "hollerhollow@mailbarn.net"

Nice to have
- Use your imagination with negative space, partial graffics, etc. Keep in mind you can kind of see through the card

Should not have
- Do not change colors of chevrons

```html
<!DOCTYPE html>
<html lang="en">
<head>
<meta charset="utf-8">
<title>Holler Hollow Outfitters – Business Card</title>
<link rel="stylesheet" href="https://fonts.googleapis.com/css2?family=Bebas+Neue&family=Roboto:wght@400;500;700&display=swap">
<style>
  :root {
    --backdrop: #bfbfbf;
    --card-top: #fdfdfd;
    --card-mid: #c9c8c9;
    --card-bottom: #6f6e70;
    --brand-red: #d8212a;
    --brand-yellow: #f6cf3f;
    --ink: #141414;
    --night: #000000;
    --paper: #ffffff;
  }
  html, body {
    margin: 0;
    width: 1200px;
    height: 1200px;
    overflow: hidden;
    background: var(--backdrop);
  }
  .card {
    position: absolute;
    left: 162px;
    top: 350px;
    width: 876px;
    height: 500px;
    border-radius: 18px;
    overflow: hidden;
    background: linear-gradient(180deg, var(--card-top) 0%, #e6e5e6 18%, var(--card-mid) 45%, #9d9b9d 72%, var(--card-bottom) 100%);
    font-family: "Roboto", sans-serif;
  }
  .brand {
    position: absolute;
    left: 92px;
    top: 118px;
    width: 260px;
    text-align: center;
  }
  .brand-dot {
    display: block;
    width: 84px;
    height: 84px;
    margin: 0 auto 18px;
    border-radius: 50%;
    background: var(--brand-yellow);
  }
  .brand-name {
    margin: 0;
    font-family: "Roboto", sans-serif;
    font-weight: 700;
    font-size: 25px;
    line-height: 1.15;
    letter-spacing: 1px;
    color: var(--brand-red);
  }
  .person {
    position: absolute;
    left: 442px;
    top: 122px;
  }
  .person-name {
    margin: 0;
    font-family: "Bebas Neue", sans-serif;
    font-size: 49px;
    line-height: 1;
    letter-spacing: 1px;
    color: var(--brand-red);
  }
  .person-role {
    margin: 0;
    font-size: 20px;
    letter-spacing: 1px;
    color: var(--ink);
  }
  .contacts {
    position: absolute;
    left: 446px;
    top: 256px;
    margin: 0;
    padding: 0;
    list-style: none;
  }
  .contacts li {
    display: flex;
    align-items: center;
    height: 36px;
    font-size: 21px;
    letter-spacing: 1.2px;
    color: var(--ink);
  }
  .contacts svg {
    width: 20px;
    height: 20px;
    margin-right: 18px;
    fill: var(--brand-red);
  }
  .footer-wave {
    position: absolute;
    left: 0;
    top: 0;
    width: 876px;
    height: 500px;
  }
  .motto {
    position: absolute;
    margin: 0;
    font-size: 20px;
    font-weight: 500;
    letter-spacing: 1.1px;
    color: var(--paper);
    white-space: nowrap;
  }
  .motto-first { left: 140px; top: 452px; }
  .motto-second { left: 444px; top: 466px; }
</style>
</head>
<body>
  <main class="card">
    <svg class="footer-wave" viewBox="0 0 876 500" aria-hidden="true">
      <path fill="var(--brand-red)" d="M0 404 C150 394 350 414 560 444 L720 452 C800 450 860 430 876 410 L876 500 L0 500 Z"/>
      <path fill="var(--night)" d="M0 438 C150 412 400 425 700 452 C800 458 860 446 876 440 L876 500 L0 500 Z"/>
      <path fill="none" stroke="var(--brand-yellow)" stroke-width="3" d="M0 438 C150 412 400 425 700 452 C800 458 860 446 876 440"/>
    </svg>

    <div class="brand">
      <span class="brand-dot"></span>
      <p class="brand-name">HOLLER HOLLOW<br>OUTFITTERS</p>
    </div>

    <div class="person">
      <h1 class="person-name">WADE CALLAHAN</h1>
      <p class="person-role">Director</p>
    </div>

    <ul class="contacts">
      <li>
        <svg viewBox="0 0 24 24" aria-hidden="true"><path d="M6.6 10.8c1.4 2.8 3.8 5.1 6.6 6.6l2.2-2.2c.3-.3.7-.4 1-.2 1.1.4 2.3.6 3.6.6.6 0 1 .4 1 1V20c0 .6-.4 1-1 1C10.6 21 3 13.4 3 4c0-.6.4-1 1-1h3.5c.6 0 1 .4 1 1 0 1.3.2 2.5.6 3.6.1.3 0 .7-.2 1L6.6 10.8z"/></svg>
        000 000 0000
      </li>
      <li>
        <svg viewBox="0 0 24 24" aria-hidden="true"><path d="M2 5h20v2.2l-10 6-10-6z"/><path d="M2 9.5l10 6 10-6V19H2z"/></svg>
        hollerhollow@mailbarn.net
      </li>
      <li>
        <svg viewBox="0 0 24 24" aria-hidden="true"><path d="M12 2a10 10 0 1 0 0 20 10 10 0 0 0 0-20zm7.9 9h-3.4a15 15 0 0 0-1.4-6.2A8 8 0 0 1 19.9 11zM12 4c.9 1.2 2.3 3.7 2.5 7h-5C9.7 7.7 11.1 5.2 12 4zM8.9 4.8A15 15 0 0 0 7.5 11H4.1a8 8 0 0 1 4.8-6.2zM4.1 13h3.4a15 15 0 0 0 1.4 6.2A8 8 0 0 1 4.1 13zM12 20c-.9-1.2-2.3-3.7-2.5-7h5c-.2 3.3-1.6 5.8-2.5 7zm3.1-.8a15 15 0 0 0 1.4-6.2h3.4a8 8 0 0 1-4.8 6.2z"/></svg>
        www.hollerhollow.net
      </li>
    </ul>

    <p class="motto motto-first">Built for the back roads.....</p>
    <p class="motto motto-second">Dressed for the DIRT we love!!</p>
  </main>
</body>
</html>
```